Family Medicine Clinic Needs Mailchimp Newsletter Template

Looking for a responsive mailchimp template that matches the theme and overall look/feel of our website brookvaleclinic.com.

I'm looking for a professional, clean, simple, minimalist, bold design.
Colors would ideally be greens and blues, cool tones, muted colors, or graytones.

See attached word document for content for the upcoming newsletter

Can see prior newsletter content here:
http://brookvaleclinic.com/ourresources/newsletter-archive/

I have attached a copy of our brochure to see a sample of what we offer

The desired newsletter title would be:
The Brook Note
Looking for a great banner for that

Looking for basically 1 main photo area per text area for future templates

Under September is Spine Focus Season want links to our different services I mention

Under the videos section would like a video gallery of sorts that have links to the videos

Lumaderm image ad needs to be redone

Would like a button to take to schedule an appointment and patient portal
Easily visible phone number
Would like to have several sections with buttons to find out more

Would like feedback question at bottom
Rated 7-10 would forward to
https://lnkvo.net/qX8pZa

1-6 would send email to us

Reason: I have now guaranteed payment so I am giving a few more days for those designers that still want to submit a design

Clinic

Coded - Design and coding required

```html
<!DOCTYPE html>
<html lang="en">
<head>
<meta charset="utf-8">
<title>The Brook Note — Brookvale Family Medicine</title>
<link href="https://fonts.googleapis.com/css2?family=Open+Sans:ital,wght@0,400;0,600;0,700;1,400&display=swap" rel="stylesheet">
<style>
:root{
  --blue:#2f9bd6;
  --blue-dark:#1f6fa3;
  --green:#7db83a;
  --green-dark:#5f9a22;
  --ink:#333;
  --muted:#777;
  --light:#f2f2f2;
  --white:#fff;
}
*{box-sizing:border-box;margin:0;padding:0}
html,body{width:1200px;height:3435px;overflow:hidden}
body{font-family:"Open Sans",Arial,sans-serif;color:var(--ink);background:var(--white);position:relative}
.abs{position:absolute}
.pill{display:flex;align-items:center;justify-content:center;border-radius:30px;font-weight:700;text-transform:uppercase;letter-spacing:.5px}
.btn-green{background:linear-gradient(var(--green),var(--green-dark));color:var(--white);font-size:14px}

/* header */
.site-header{top:0;left:0;width:1200px;height:115px;background:var(--white)}
.brand{left:76px;top:30px;display:flex;align-items:center;gap:12px}
.brand-mark{width:22px;height:22px;border-radius:50%;background:var(--green)}
.brand-name{font-size:28px;font-weight:700;color:var(--blue-dark)}
.portal-tab{left:870px;top:0;width:240px;height:46px;background:var(--blue);border-radius:0 0 14px 14px;color:var(--white);font-size:13px;font-weight:700;display:flex;align-items:center;justify-content:center;gap:8px;letter-spacing:.5px}
.schedule-btn{left:497px;top:63px;width:270px;height:43px}
.call{left:800px;top:66px;display:flex;align-items:center;gap:12px;font-size:17px;font-weight:600;color:var(--ink)}
.call strong{font-size:23px;color:var(--blue-dark)}

/* hero */
.hero{top:115px;left:0;width:1200px;height:510px;background:linear-gradient(100deg,#6fb4e6 0%,#a8d3f1 45%,#e9d6c4 70%,#cfe4f6 100%)}
.hero-title{left:78px;top:185px;font-size:70px;font-weight:700;color:var(--white);-webkit-text-stroke:2px #1c3d57;letter-spacing:1px}

/* awareness */
.section-title{width:1200px;text-align:center;font-weight:700;font-size:33px}
.awareness-title{top:662px;color:var(--blue-dark)}
.awareness-sub{top:723px;width:1200px;text-align:center;font-size:24px;font-weight:600;color:var(--ink)}
.point{top:776px;width:410px;display:flex;gap:18px;font-size:14px;line-height:28px;color:#555}
.point svg{flex:none;margin-top:7px}
.awareness-btn{left:517px;top:893px;width:166px;height:44px}

/* services */
.services{top:990px;left:0;width:1200px;height:522px;background:var(--blue)}
.services-title{top:1027px;color:var(--white)}
.service{width:260px;text-align:center;color:var(--white);font-size:16px;font-weight:700}
.service svg{display:block;margin:0 auto 14px}
.services-btn{left:517px;top:1412px;width:166px;height:44px}

/* video */
.video-title{top:1549px;color:var(--blue-dark)}
.video{top:1640px;width:462px;height:276px;border:5px solid #d6d6d6}
.video .fill{width:100%;height:100%}
.play{left:50%;top:50%;width:62px;height:62px;margin:-31px 0 0 -31px;border:5px solid var(--white);border-radius:50%;background:rgba(0,0,0,.25)}
.play::after{content:"";position:absolute;left:21px;top:13px;border-left:20px solid var(--white);border-top:13px solid transparent;border-bottom:13px solid transparent}
.arrow{font-size:44px;color:#bbb;font-weight:400}

/* testimonials */
.testimonials{top:1978px;left:0;width:1200px;height:389px;background:var(--green)}
.testimonials-title{top:2017px;color:var(--white)}
.quote{top:2100px;width:190px;color:var(--white);font-size:13px;line-height:25px;font-style:italic}
.quote .who{margin-top:14px;font-style:normal;font-weight:700;color:#d9f0b5;font-size:12px;line-height:18px}
.quote .loc{font-size:12px;line-height:18px}

/* before & after */
.results{top:2367px;left:0;width:1200px;height:413px;background:var(--light)}
.results-title{top:2399px;color:var(--blue-dark)}
.pair{top:2465px;width:332px;height:187px;display:flex;gap:2px}
.pair .half{flex:1;display:flex;flex-direction:column}
.pair .photo{flex:1}
.pair .label{height:42px;background:var(--blue);color:var(--white);font-size:13px;font-weight:700;display:flex;align-items:center;justify-content:center}
.results-btn{left:517px;top:2683px;width:166px;height:44px}

/* feedback */
.feedback{top:2780px;left:0;width:1200px;height:410px;background:var(--blue)}
.feedback-title{top:2822px;color:var(--white)}
.comment{left:77px;top:2912px;width:1048px;height:140px;border:2px solid #a8d5f0;border-radius:10px;padding:12px 16px;font-size:12px;color:#d8eefa}
.submit{left:77px;top:3083px;width:166px;height:44px;background:var(--white);color:var(--ink);font-size:13px}

/* footer */
.footer-brand{top:3252px;left:0;width:1200px;display:flex;justify-content:center;align-items:center;gap:12px}
.copyright{top:3306px;width:1200px;text-align:center;font-size:13px;color:var(--muted)}
.social{top:3340px;left:0;width:1200px;display:flex;justify-content:center;gap:16px}
.social span{width:20px;height:20px;border-radius:50%;background:#555}
</style>
</head>
<body>

<header class="site-header abs">
  <div class="brand abs"><span class="brand-mark"></span><span class="brand-name">Brookvale Family Medicine</span></div>
  <div class="portal-tab abs">
    <svg width="13" height="13" viewBox="0 0 14 14"><circle cx="7" cy="4" r="3.3" fill="#fff"/><path d="M1 14c0-4 2.7-6 6-6s6 2 6 6z" fill="#fff"/></svg>
    PATIENT PORTAL
  </div>
  <div class="schedule-btn pill btn-green abs">Schedule an Appointment</div>
  <div class="call abs">
    <svg width="18" height="18" viewBox="0 0 24 24"><path d="M6.6 10.8a15 15 0 0 0 6.6 6.6l2.2-2.2c.3-.3.7-.4 1-.2 1.1.4 2.3.6 3.6.6.6 0 1 .4 1 1V20c0 .6-.4 1-1 1A17 17 0 0 1 3 4c0-.6.4-1 1-1h3.5c.6 0 1 .4 1 1 0 1.3.2 2.5.6 3.6.1.3 0 .7-.2 1z" fill="#333"/></svg>
    <span>CALL US NOW: <strong>(555) 204-7781</strong></span>
  </div>
</header>

<section class="hero abs" role="img" aria-label="Smiling couple outdoors against a blue sky">
  <h1 class="hero-title abs">The Brook Note</h1>
</section>

<h2 class="section-title awareness-title abs">September is Spine Focus Season</h2>
<p class="awareness-sub abs">What You Need to Know</p>
<div class="point abs" style="left:165px">
  <svg width="14" height="14" viewBox="0 0 14 14"><circle cx="7" cy="7" r="7" fill="var(--green)"/><path d="M3.5 7.2l2.3 2.2 4.6-4.8" stroke="#fff" stroke-width="1.8" fill="none"/></svg>
  <p>Nearly 100 million Americans experience chronic pain more than those who have diabetes, heart disease and cancer combined..</p>
</div>
<div class="point abs" style="left:612px">
  <svg width="14" height="14" viewBox="0 0 14 14"><circle cx="7" cy="7" r="7" fill="var(--green)"/><path d="M3.5 7.2l2.3 2.2 4.6-4.8" stroke="#fff" stroke-width="1.8" fill="none"/></svg>
  <p>Pain is a warning sign that indicates a problem that needs attention, don't just mask your symptoms, let us help try to get to the root of your issue.</p>
</div>
<div class="awareness-btn pill btn-green abs">View More</div>

<section class="services abs"></section>
<h2 class="section-title services-title abs">Our Services</h2>
<div class="service abs" style="left:57px;top:1105px"><svg width="60" height="60" viewBox="0 0 60 60" fill="none" stroke="#fff" stroke-width="3"><rect x="8" y="34" width="44" height="8"/><path d="M14 42v12M46 42v12"/><circle cx="30" cy="14" r="7"/><path d="M22 34v-8h16v8"/></svg>Osteopathic Manipulation</div>
<div class="service abs" style="left:273px;top:1105px"><svg width="60" height="60" viewBox="0 0 60 60" fill="none" stroke="#fff" stroke-width="3"><rect x="8" y="36" width="44" height="7"/><path d="M14 43v11M46 43v11M20 10l6 24M32 8l-2 26M42 12l-8 22"/></svg>Acupuncture</div>
<div class="service abs" style="left:603px;top:1105px"><svg width="60" height="60" viewBox="0 0 60 60" fill="none" stroke="#fff" stroke-width="3"><path d="M18 52h24M30 52V20"/><circle cx="30" cy="12" r="6"/><path d="M18 30h24"/></svg>Prolotherapy</div>
<div class="service abs" style="left:877px;top:1105px"><svg width="60" height="60" viewBox="0 0 60 60" fill="none" stroke="#fff" stroke-width="3"><circle cx="30" cy="30" r="22"/><path d="M30 18v24M18 30h24"/></svg>PRP</div>
<div class="service abs" style="left:57px;top:1245px"><svg width="60" height="60" viewBox="0 0 60 60" fill="none" stroke="#fff" stroke-width="3"><path d="M10 50l30-30M34 14l12 12M42 10l8 8M16 44l-6 6"/></svg>Stem Cell Injections</div>
<div class="service abs" style="left:273px;top:1245px"><svg width="60" height="60" viewBox="0 0 60 60" fill="none" stroke="#fff" stroke-width="3"><path d="M30 6v48M22 14h16M22 26h16M22 38h16M22 50h16"/></svg>Spinal Decompression</div>
<div class="service abs" style="left:603px;top:1245px"><svg width="60" height="60" viewBox="0 0 60 60" fill="none" stroke="#fff" stroke-width="3"><path d="M16 50c-5-8 5-12 0-20s5-12 0-20M30 50c-5-8 5-12 0-20s5-12 0-20M44 50c-5-8 5-12 0-20s5-12 0-20"/></svg>Infrared Sauna</div>
<div class="service abs" style="left:877px;top:1245px"><svg width="60" height="60" viewBox="0 0 60 60" fill="none" stroke="#fff" stroke-width="3"><rect x="14" y="16" width="12" height="38" rx="5"/><rect x="34" y="16" width="12" height="38" rx="5"/><path d="M20 16V8M40 16V8M16 8h28"/></svg>Hyperbaric Oxygen</div>
<div class="services-btn pill btn-green abs">View More</div>

<h2 class="section-title video-title abs">Video Gallery</h2>
<div class="arrow abs" style="left:74px;top:1745px">&#8249;</div>
<div class="video abs" style="left:120px">
  <div class="fill" role="img" aria-label="Clinic building entrance" style="background:linear-gradient(#8f8a86,#6e6a67)"></div>
  <span class="play abs"></span>
</div>
<div class="video abs" style="left:625px">
  <div class="fill" role="img" aria-label="Relaxed woman resting outdoors" style="background:linear-gradient(120deg,#c9c6c0,#9fa3a6)"></div>
  <span class="play abs"></span>
</div>
<div class="arrow abs" style="left:1108px;top:1745px">&#8250;</div>

<section class="testimonials abs"></section>
<h2 class="section-title testimonials-title abs">Testimonials</h2>
<div class="quote abs" style="left:77px">“ Aliquam molestie, mi et imperdiet euismod, dui purus auctor tellus, et ante. congue, neque ac obortis mauris varius mi....”<div class="who">- NAME HEADING</div><div class="loc">Location</div></div>
<div class="quote abs" style="left:292px">“ Aliquam molestie, mi et imperdiet euismod, dui purus auctor tellus, et ante. congue, neque ac obortis mauris varius mi....”<div class="who">- NAME HEADING</div><div class="loc">Location</div></div>
<div class="quote abs" style="left:507px">“ Aliquam molestie, mi et imperdiet euismod, dui purus auctor tellus, et ante. congue, neque ac obortis mauris varius mi....”<div class="who">- NAME HEADING</div><div class="loc">Location</div></div>
<div class="quote abs" style="left:722px">“ Aliquam molestie, mi et imperdiet euismod, dui purus auctor tellus, et ante. congue, neque ac obortis mauris varius mi....”<div class="who">- NAME HEADING</div><div class="loc">Location</div></div>
<div class="quote abs" style="left:937px">“ Aliquam molestie, mi et imperdiet euismod, dui purus auctor tellus, et ante. congue, neque ac obortis mauris varius mi....”<div class="who">- NAME HEADING</div><div class="loc">Location</div></div>

<section class="results abs"></section>
<h2 class="section-title results-title abs">Before &amp; After</h2>
<div class="arrow abs" style="left:38px;top:2520px">&#8249;</div>
<div class="pair abs" style="left:75px">
  <div class="half"><div class="photo" role="img" aria-label="Eye area before treatment" style="background:linear-gradient(#d9b8a4,#c29a85)"></div><div class="label">Before</div></div>
  <div class="half"><div class="photo" role="img" aria-label="Eye area after treatment" style="background:linear-gradient(#e3c7b4,#cfa893)"></div><div class="label">After</div></div>
</div>
<div class="pair abs" style="left:433px">
  <div class="half"><div class="photo" role="img" aria-label="Forehead before treatment" style="background:linear-gradient(#b9aca3,#d6c2b4)"></div><div class="label">Before</div></div>
  <div class="half"><div class="photo" role="img" aria-label="Forehead after treatment" style="background:linear-gradient(#c2b5ab,#e0ccbe)"></div><div class="label">After</div></div>
</div>
<div class="pair abs" style="left:795px">
  <div class="half"><div class="photo" role="img" aria-label="Face before treatment" style="background:linear-gradient(#e6c3a6,#d2a586)"></div><div class="label">Before</div></div>
  <div class="half"><div class="photo" role="img" aria-label="Face after treatment" style="background:linear-gradient(#ebcbb0,#d9ae90)"></div><div class="label">After</div></div>
</div>
<div class="arrow abs" style="left:1140px;top:2520px">&#8250;</div>
<div class="results-btn pill btn-green abs">View More</div>

<section class="feedback abs"></section>
<h2 class="section-title feedback-title abs">Enter Your Feedback</h2>
<div class="comment abs">Comment</div>
<div class="submit pill abs">Submit</div>

<footer>
  <div class="footer-brand abs"><span class="brand-mark"></span><span class="brand-name">Brookvale Family Medicine</span></div>
  <p class="copyright abs">Copyright © 2017. Company Name. All Rights Reserved.</p>
  <div class="social abs"><span></span><span></span><span></span><span></span><span></span></div>
</footer>

</body>
</html>
```